Letterhead Design for Law Firm

**Edit: I have added the photo of a bottom that I like.

------
We are looking for a re-design of our new letterhead. The letterhead is for a law firm and will be used for digital and traditionally printed correspondence.

Here are some suggestions:

- Please use colours are #8ec900 and simple black.
- Please do not use any type of "waves" at the bottom of the page. This is not in style at all.
- Please stay modern yet conservative.
- Please use font Segoe UI Light or similar if you can
- Avoid clipart or illustrations.
- Utilize ample white space in the layout so the design looks clean and information is easy to read at a glance. Don't overcrowd the letterhead.
- Make sure the letterhead design is consistent with our brand identity (see brambleford.ca)
-Please, no black headers or footers.

I am attaching my current letterhead and signature for your convenience.

Remember, the letterhead is an extension of our professional identity. We are a successful firm and trial lawyers who correspond with insurers, judges, lawyers, courts, clients, etc. Make it new, modern, attractive, yet powerful and conservative.

It needs to be easily printable. I would like the bleed removed in print so the black bar the bottom crosses the page (but the text is not near the edges)

Target Market(s)

Clients, Government Offices, Judiciary, Lawyers, Insurance Companies, Colleagues.

Industry/Entity Type

Law

Font styles to use
Other font styles liked:
• Segoe UI LIght, Calibri Light,

Colors
00AB8E
00BBA5
67D7C9
C6EFE9
E9F9F6

Requirements
Must have
• Everything that is on the letterhead now.
Nice to have
• Cutting Edge design, yet conservative.
Should not have
• law firm cliche design, images,

```html
<!DOCTYPE html>
<html lang="en">
<head>
<meta charset="utf-8">
<title>Harrowgate Letterhead</title>
<link rel="stylesheet" href="https://fonts.googleapis.com/css2?family=Open+Sans:wght@300;400&display=swap">
<style>
  :root {
    --backdrop: #d4d4d4;
    --paper: #ffffff;
    --navy: #002454;
    --lime: #8ec900;
    --ink-light: #ffffff;
  }
  * { margin: 0; padding: 0; box-sizing: border-box; }
  html, body {
    width: 1200px;
    height: 848px;
    overflow: hidden;
    background: var(--backdrop);
    font-family: "Open Sans", "Segoe UI", sans-serif;
  }
  .letterhead {
    position: absolute;
    left: 291px;
    top: 24px;
    width: 618px;
    height: 800px;
    background: var(--paper);
    box-shadow: 0 4px 14px rgba(0, 0, 0, 0.25);
    overflow: hidden;
  }
  .footer-band {
    position: absolute;
    left: 0;
    bottom: 0;
    width: 618px;
    height: 170px;
  }
  .footer-band path { fill: var(--navy); }
  .contact {
    position: absolute;
    color: var(--ink-light);
    font-weight: 300;
    font-size: 10.5px;
    line-height: 15px;
    list-style: none;
  }
  .contact li {
    display: flex;
    align-items: flex-start;
    gap: 6px;
  }
  .contact svg {
    width: 9px;
    height: 9px;
    margin-top: 3px;
    flex: none;
    fill: var(--lime);
  }
  .contact-direct { left: 196px; top: 722px; }
  .contact-address { left: 326px; top: 708px; }
  .brand {
    position: absolute;
    left: 460px;
    top: 684px;
    width: 140px;
    text-align: center;
    color: var(--ink-light);
  }
  .brand-name {
    font-weight: 400;
    font-size: 21px;
    letter-spacing: 1px;
    line-height: 1;
    padding-bottom: 4px;
    border-bottom: 1px solid var(--lime);
  }
  .brand-tagline {
    font-weight: 300;
    font-size: 6.6px;
    letter-spacing: 0.9px;
    margin-top: 3px;
    text-transform: uppercase;
  }
</style>
</head>
<body>
  <main class="letterhead">
    <svg class="footer-band" viewBox="0 0 618 170" preserveAspectRatio="none" aria-hidden="true">
      <path d="M0 150 Q260 60 618 0 L618 170 L0 170 Z"/>
    </svg>

    <ul class="contact contact-direct">
      <li>
        <svg viewBox="0 0 10 10" aria-hidden="true"><path d="M2 0.5 L3.6 2.6 L2.8 3.6 Q4 6 6.4 7.2 L7.4 6.4 L9.5 8 L8.4 9.5 Q1 8 0.5 1.6 Z"/></svg>
        <span>905-555-0142</span>
      </li>
      <li>
        <svg viewBox="0 0 10 10" aria-hidden="true"><path d="M0 2 H10 V8.5 H0 Z M0.8 2.6 L5 5.6 L9.2 2.6" stroke="#002454" stroke-width="0.8"/></svg>
        <span>info@brambleford.ca</span>
      </li>
      <li>
        <svg viewBox="0 0 10 10" aria-hidden="true"><circle cx="5" cy="5" r="4.5"/></svg>
        <span>www.brambleford.ca</span>
      </li>
    </ul>

    <ul class="contact contact-address">
      <li>
        <svg viewBox="0 0 10 10" aria-hidden="true"><path d="M5 0 A3.6 3.6 0 0 1 8.6 3.6 Q8.6 6 5 10 Q1.4 6 1.4 3.6 A3.6 3.6 0 0 1 5 0 Z M5 2.2 A1.4 1.4 0 1 0 5.01 2.2 Z"/></svg>
        <span>48 Alder Street West<br>Suite 1210, Hamilton<br>ON L8P 2B7, Canada</span>
      </li>
    </ul>

    <div class="brand">
      <div class="brand-name">HARROWGATE</div>
      <div class="brand-tagline">Personal Injury Lawyers</div>
    </div>
  </main>
</body>
</html>
```